Homeowners Insurance Provider Website

We are selling homeowners insurance policy / tenants Policy/Flood Insurance in USA in few states and planning expand nationally.

Our target audience are two folds: Customers (Buy policies) and Insurance Agents who wants to work with us to sell our policies to customers. But website should focus 80% on customers and 20% on agents. So, more customer focused user experience. Please note that there is no direct buy option for customers. They always go through insurance agents.

Customer focused, educational that makes buyer journey easy. We don’t want to come off as trying sell something as there is no direct sales involved from website.

Target Market(s)

Homeowners in USA and Insurance agent who sells these insurance.

Industry/Entity Type

Insurance

Number of Pages Required

4 page

Font styles to use
Other font styles liked:
• Open to suggestions

Colors

Designer to choose colors to be used in the design.

Requirements
Must have
• Three most important things: Trustworthy, Authentic, Simple
• Please use colors form logo and grays
• We like: www.brightmeadow.com
• https://www.harborlinden.com/
• We need Agent Look up tool on home page similar to what is shown on example sites.
• Design:
• Home Page - Open to Ideas
• Insurance (Products) Landing Page - Info similar to: https://www.harborlinden.com/insurance/
• Agents Page - https://www.harborlinden.com/agents/
• Claims Page - Information similar to: https://www.harborlinden.com/claims-center/
• Site Navigation:
• Home
• Insurance
• Claims
• Agents
• About Us
• Contact Us
Nice to have
• Elegant, minimal and clean design that reflects trust and authenticity.
Should not have
• Slider or rotating images - prefer flat design. Not over powering design.

```html
<!DOCTYPE html>
<html lang="en">
<head>
<meta charset="utf-8">
<title>Keystead Insurance Co. — Home</title>
<link href="https://fonts.googleapis.com/css2?family=Source+Sans+3:wght@400;600;700&display=swap" rel="stylesheet">
<style>
:root{
  --navy:#1c3f8f;
  --navy-deep:#173577;
  --red:#d7202b;
  --ink:#2f2f2f;
  --gray:#6b6b6b;
  --light:#f4f4f4;
  --footer:#1b1b1b;
  --white:#ffffff;
}
*{box-sizing:border-box;margin:0;padding:0}
html,body{width:936px;height:1200px;overflow:hidden;background:var(--white)}
body{font-family:"Source Sans 3",Arial,sans-serif;color:var(--ink);position:relative}
a{color:inherit;text-decoration:none}

/* hero */
.hero{position:absolute;left:0;top:0;width:936px;height:526px;
  background:linear-gradient(90deg,#cfc6bd 0%,#e6ded6 22%,#f1efed 45%,#f6f6f6 70%,#f2f2f2 100%)}
.hero-photo{position:absolute;left:0;top:60px;width:420px;height:466px;
  background:radial-gradient(ellipse at 50% 40%,#e9ddd2 0%,#d8cabd 45%,rgba(230,224,218,0) 75%)}
.site-header{position:absolute;left:134px;top:10px;width:667px;height:36px;display:flex;align-items:center}
.brand{display:flex;align-items:center;gap:8px}
.brand-mark{width:26px;height:26px;background:var(--navy);border-radius:4px}
.brand-name{font-size:15px;font-weight:700;color:var(--navy);letter-spacing:.5px;line-height:1}
.main-nav{display:flex;gap:14px;margin-left:58px;font-size:10px;color:#3a3a3a}
.main-nav .active{color:var(--red)}
.header-actions{margin-left:auto;display:flex;gap:3px}
.btn-sm{height:26px;padding:0 11px;display:flex;align-items:center;gap:4px;font-size:10px;font-weight:600;color:#fff;border-radius:2px}
.btn-blue{background:var(--navy)}
.btn-red{background:var(--red)}

.finder{position:absolute;left:440px;top:146px;width:340px;text-align:center}
.finder h1{font-size:21px;font-weight:600;color:#2b2b2b}
.finder p{font-size:11px;color:#444;line-height:15px;margin-top:9px}
.finder-form{display:flex;justify-content:center;gap:6px;margin-top:19px}
.zip{width:115px;height:32px;border:1px solid #d6d6d6;background:#fff;font-size:10px;color:#888;padding-left:10px;display:flex;align-items:center}
.btn-find{height:32px;padding:0 12px;background:var(--red);color:#fff;font-size:11px;font-weight:600;display:flex;align-items:center;gap:6px;border-radius:2px}

.product{position:absolute;top:370px;width:140px;height:140px;border-radius:50%;background:rgba(255,255,255,.75);
  box-shadow:0 2px 8px rgba(0,0,0,.15);display:flex;align-items:center;justify-content:center}
.product-inner{width:126px;height:126px;border-radius:50%;background:radial-gradient(circle at 50% 35%,#2453a8,var(--navy-deep));
  color:#fff;display:flex;flex-direction:column;align-items:center;justify-content:center;text-align:center;font-size:11px;font-weight:600;line-height:12px}
.product-inner svg{margin-bottom:10px}

/* claims band */
.claims-band{position:absolute;left:0;top:526px;width:936px;height:70px;background:var(--navy-deep);color:#fff}
.claims-band p{position:absolute;left:134px;top:18px;width:540px;font-size:13px;font-weight:600;line-height:16px}
.claims-band .btn-sm{position:absolute;left:712px;top:22px;height:26px;padding:0 11px}

/* insights */
.insights{position:absolute;left:134px;top:626px;width:667px;text-align:center}
.insights h2{font-size:21px;font-weight:600;color:#2b2b2b}
.insights .lead{font-size:11px;color:#555;margin-top:7px}
.insights .lead a{color:var(--red);text-decoration:underline}
.cards{display:flex;gap:17px;margin-top:23px;text-align:left}
.card{width:211px}
.card-img{height:152px;width:211px}
.card h3{font-size:14px;font-weight:400;color:#2b2b2b;margin-top:16px;line-height:14px}
.card p{font-size:9px;color:#777;line-height:14px;margin-top:6px}

/* footer */
.site-footer{position:absolute;left:0;top:973px;width:936px;height:227px;background:var(--footer);color:#fff}
.f-col{position:absolute;top:31px}
.f-col h4{font-size:11px;font-weight:600;margin-bottom:10px}
.f-col li{list-style:none;font-size:9px;line-height:15px;color:#ddd}
.phone{font-size:13px;font-weight:600;line-height:14px}
.mail{font-size:9px;color:#ddd}
.socials{display:flex;gap:4px;margin-top:12px}
.socials span{width:24px;height:24px;border:1.5px solid #fff;border-radius:50%}
.btn-outline{margin-top:14px;width:110px;height:31px;border:1.5px solid #fff;border-radius:2px;display:flex;align-items:center;justify-content:center;gap:6px;font-size:11px;font-weight:600}
.legal{position:absolute;left:0;top:172px;width:936px;text-align:center;font-size:9px;line-height:15px;color:#ddd}
</style>
</head>
<body>

<section class="hero">
  <div class="hero-photo" role="img" aria-label="Smiling woman sitting on a bright bed with a laptop and a cup"></div>

  <header class="site-header">
    <a class="brand" href="#"><span class="brand-mark"></span><span class="brand-name">KEYSTEAD INSURANCE CO.</span></a>
    <nav class="main-nav">
      <a class="active" href="#">Home</a><a href="#">Insurance</a><a href="#">About Us</a><a href="#">Claims</a><a href="#">Agents</a><a href="#">Contact Us</a>
    </nav>
    <div class="header-actions">
      <a class="btn-sm btn-blue" href="#">
        <svg width="9" height="9" viewBox="0 0 10 10" fill="#fff"><circle cx="5" cy="3" r="2.4"/><path d="M0.5 10c0-3 2-4.5 4.5-4.5S9.5 7 9.5 10z"/></svg>Careers</a>
      <a class="btn-sm btn-red" href="#">
        <svg width="8" height="9" viewBox="0 0 8 10" fill="#fff"><rect x="0" y="4" width="8" height="6" rx="1"/><path d="M2 4V2.8a2 2 0 0 1 4 0V4" stroke="#fff" stroke-width="1.3" fill="none"/></svg>Login</a>
    </div>
  </header>

  <div class="finder">
    <h1>Find an Agent</h1>
    <p>Talk to one of our local independent agencies to get a quote,<br>ask questions about coverage options &amp; more!</p>
    <div class="finder-form">
      <div class="zip">ZIP Code</div>
      <a class="btn-find" href="#">
        <svg width="14" height="14" viewBox="0 0 14 14" fill="none" stroke="#fff" stroke-width="1.3"><circle cx="8" cy="6" r="5"/><path d="M4.5 9.5L1 13"/><circle cx="8" cy="5" r="1.4"/><path d="M5.6 8.4c.6-1.2 4.2-1.2 4.8 0"/></svg>
        Find an Agent</a>
    </div>
  </div>

  <a class="product" href="#" style="left:141px">
    <span class="product-inner">
      <svg width="38" height="36" viewBox="0 0 38 36" fill="#fff"><path d="M19 2L2 17h5v17h9V24h6v10h9V17h5z"/></svg>Homeowners</span>
  </a>
  <a class="product" href="#" style="left:312px">
    <span class="product-inner">
      <svg width="36" height="38" viewBox="0 0 36 38" fill="#fff"><path d="M6 4h24v34H22v-7h-8v7H6z"/><g fill="#1d44931"><rect x="10" y="8" width="4" height="4" fill="#1f4a9c"/><rect x="16" y="8" width="4" height="4" fill="#1f4a9c"/><rect x="22" y="8" width="4" height="4" fill="#1f4a9c"/><rect x="10" y="15" width="4" height="4" fill="#1f4a9c"/><rect x="16" y="15" width="4" height="4" fill="#1f4a9c"/><rect x="22" y="15" width="4" height="4" fill="#1f4a9c"/><rect x="10" y="22" width="4" height="4" fill="#1f4a9c"/><rect x="16" y="22" width="4" height="4" fill="#1f4a9c"/><rect x="22" y="22" width="4" height="4" fill="#1f4a9c"/></g></svg>Renters/Condo</span>
  </a>
  <a class="product" href="#" style="left:483px">
    <span class="product-inner">
      <svg width="46" height="36" viewBox="0 0 46 36" fill="#fff"><path d="M17 2L1 16h4v18h22V16h4z"/><rect x="10" y="20" width="5" height="5" fill="#1f4a9c"/><rect x="18" y="20" width="5" height="5" fill="#1f4a9c"/><path d="M36 8c2 5 8 9 8 17a8 8 0 0 1-16 0c0-4 3-6 3-10 2 2 3 4 3 6 2-3 2-8 2-13z"/></svg>Dwelling Fire</span>
  </a>
  <a class="product" href="#" style="left:655px">
    <span class="product-inner">
      <svg width="38" height="40" viewBox="0 0 38 40" fill="none" stroke="#fff" stroke-width="2"><path d="M19 2a9 9 0 0 1 9 9c0 7-9 16-9 16S10 18 10 11a9 9 0 0 1 9-9z" fill="#fff"/><circle cx="19" cy="11" r="3.5" fill="#1f4a9c" stroke="none"/><path d="M9 26L3 38h32l-6-12"/></svg>Agent Locator<br>Tool</span>
  </a>
</section>

<section class="claims-band">
  <p>To make it easy and stress free as possible, we have quick online form for you to report a claim or you can call us at 1-866-555-0142</p>
  <a class="btn-sm btn-red" href="#">Report a Claim</a>
</section>

<section class="insights">
  <h2>Plain Insights<sup style="font-size:10px">®</sup> by Keystead Insurance Co.</h2>
  <p class="lead">Take advantage of what we’ve learned through the years in <a href="#">Plain Insights<sup style="font-size:7px">®</sup></a></p>
  <div class="cards">
    <article class="card">
      <div class="card-img" role="img" aria-label="Businessman holding a glowing house outline in open hands" style="background:radial-gradient(circle at 50% 55%,#3f8fa8 0%,#1d3d55 45%,#142635 100%)"></div>
      <h3>DIY Home Safety Audit</h3>
      <p>Proin condimentum fermentum nunc. Etiam pharetra, erat sed fermentum feugiat velit mauris egestas quam ut aliquam massa nisl quis neque.</p>
    </article>
    <article class="card">
      <div class="card-img" role="img" aria-label="Stack of credit cards resting on banknotes" style="background:linear-gradient(135deg,#9a9790 0%,#c9c5bb 45%,#7e7a72 100%)"></div>
      <h3>Common Rental and Landlord Scams</h3>
      <p>Proin condimentum fermentum nunc. Etiam pharetra, erat sed fermentum feugiat velit mauris egestas quam ut aliquam massa nisl quis neque.</p>
    </article>
    <article class="card">
      <div class="card-img" role="img" aria-label="Dripping chrome water tap on a blue background" style="background:linear-gradient(90deg,#6cc6f2 0%,#3a9de4 50%,#8fd4f7 100%)"></div>
      <h3>How to Save Water at Home</h3>
      <p>Proin condimentum fermentum nunc. Etiam pharetra, erat sed fermentum feugiat velit mauris egestas quam ut aliquam massa nisl quis neque.</p>
    </article>
  </div>
</section>

<footer class="site-footer">
  <div class="f-col" style="left:134px">
    <h4>Contact Info</h4>
    <div class="phone">1800 555 0188</div>
    <div class="mail">info@keysteadinsurance.co</div>
    <div class="socials"><span></span><span></span><span></span><span></span></div>
  </div>
  <div class="f-col" style="left:305px">
    <h4>Our Company</h4>
    <ul><li>Home</li><li>Insurance</li><li>About Us</li><li>Claims</li><li>Agents</li></ul>
  </div>
  <div class="f-col" style="left:419px">
    <h4>Login to Your Account</h4>
    <ul><li>Agents Login</li><li>Clients login</li></ul>
    <a class="btn-outline" href="#">
      <svg width="13" height="13" viewBox="0 0 14 14" fill="none" stroke="#fff" stroke-width="1.3"><circle cx="8" cy="6" r="5"/><path d="M4.5 9.5L1 13"/></svg>Find an Agent</a>
  </div>
  <div class="f-col" style="left:573px">
    <h4>Customer Support</h4>
    <ul><li>FAQs</li><li>Resources</li><li>Report a Claim</li><li>Find an Agent</li></ul>
  </div>
  <div class="f-col" style="left:704px">
    <h4>Connect With Us</h4>
    <ul><li>Support</li><li>Careers</li></ul>
  </div>
  <div class="legal">Copyright ©2018 Keystead Insurance. All Rights Reserved<br>Terms of Use &nbsp;-&nbsp; Privacy Policy &nbsp;-&nbsp; Sitemap</div>
</footer>

</body>
</html>
```